WEB HOSTING COMPANY WHMCS THEME

The name of the web host company is "brisk maple" so i would like something professional and simple. Il let you guys chouse the colors use your imagination on this, i will need a logo and a business card design. I would also like the theme coded and installed to my whims server and last thing we need to setup the website to go live at te end i will pay extra for that. Thank you

Target Market(s)

Web Hosting Company

Contact Information for Business Card

BRISKMAPLE

Logo Text

BRISKMAPLE

Coding

Coded - Design and coding required

Number of Pages Required

5+ page

Font styles to use
Sans Serif

Requirements
Must have
• EMAIL PHONE NUMBER MOBILE NUMBER WEBSITE AND BUSINESS ADRESS

```html
<!DOCTYPE html>
<html lang="en">
<head>
<meta charset="utf-8">
<title>brisk maple — Web Hosting</title>
<link href="https://fonts.googleapis.com/css2?family=Roboto:wght@300;400;500;700&display=swap" rel="stylesheet">
<style>
:root{
  --green:#7cbd2f;
  --green-dark:#5f9a1e;
  --orange:#f7931e;
  --navy:#16212c;
  --navy-2:#243442;
  --ink:#333c44;
  --muted:#7a838b;
  --line:#e3e6e9;
  --paper:#ffffff;
  --mist:#f2f3f5;
  --teal:#27a8c4;
  --blue:#2c4f8c;
}
*{box-sizing:border-box;margin:0;padding:0}
html,body{width:1200px;height:4072px;overflow:hidden}
body{font-family:'Roboto',Arial,sans-serif;color:var(--ink);background:var(--paper);position:relative;font-size:14px}
.section{position:absolute;left:0;width:1200px}
.btn{display:inline-block;background:var(--orange);color:#fff;border-radius:22px;padding:12px 30px;font-size:15px;font-weight:500}
.title{text-align:center;font-size:34px;font-weight:400;color:var(--ink)}
.title .hl{color:var(--orange);font-weight:500}
.lede{font-size:13px;line-height:21px;color:var(--muted)}

/* header */
.header{top:0;height:130px;background:var(--paper);border-bottom:1px solid var(--line)}
.topbar{position:absolute;right:40px;top:12px;display:flex;gap:26px;font-size:13px;color:var(--ink)}
.topbar span::before{content:"";display:inline-block;width:9px;height:9px;border-radius:50%;background:var(--green);margin-right:7px}
.logo{position:absolute;left:40px;top:50px;display:flex;align-items:center;gap:12px}
.logo-dot{width:40px;height:40px;border-radius:50%;background:var(--orange)}
.logo-name{font-size:36px;font-weight:700;color:var(--green);letter-spacing:-.5px}
.nav{position:absolute;right:40px;top:76px;display:flex;gap:24px;font-size:16px}
.nav a{color:var(--ink);text-decoration:none}
.nav a.active{color:var(--orange)}

/* hero */
.hero{top:130px;height:582px;background:linear-gradient(180deg,#1b2834,#101820)}
.hero-art{position:absolute;right:60px;top:30px;width:620px;height:520px;border-radius:8px;background:radial-gradient(circle at 50% 45%,#35536a 0%,#1d2c39 60%,transparent 75%)}
.hero-copy{position:absolute;left:80px;top:350px;color:#fff}
.hero-copy .kicker{font-size:30px;font-weight:300}
.hero-copy h1{font-size:64px;font-weight:400;color:var(--green);margin:6px 0 22px}

/* features */
.features{top:712px;height:300px;display:flex;justify-content:center;gap:70px;padding-top:40px}
.feature{width:300px;text-align:center}
.feature .ico{width:120px;height:120px;border-radius:50%;margin:0 auto 20px;display:flex;align-items:center;justify-content:center}
.feature h3{font-size:18px;font-weight:400;margin-bottom:10px}
.feature p{font-size:12px;line-height:19px;color:var(--muted)}

/* pricing */
.pricing{top:1040px;height:620px;background:var(--mist);padding-top:50px}
.pricing .lede{width:1040px;margin:16px auto 0;text-align:center}
.plans{display:flex;justify-content:center;gap:0;margin-top:34px}
.plan{width:355px;background:var(--paper);text-align:center;border:1px solid var(--line)}
.plan-head{background:var(--green);color:#fff;padding:22px 0 20px}
.plan-head small{display:block;font-size:14px}
.plan-head .price{font-size:40px;font-weight:500;margin:6px 0}
.plan-head .kind{color:var(--orange);font-size:16px;font-weight:500}
.plan .lead{font-weight:700;font-size:13px;padding:16px 30px;line-height:19px}
.plan ul{list-style:none;font-size:12px;color:var(--muted)}
.plan li{padding:10px 20px;border-top:1px solid var(--line)}
.plan .btn{margin:20px 0 24px;font-size:14px;padding:10px 26px}
.plan.featured{background:var(--navy-2);color:#fff;border-color:var(--navy-2)}
.plan.featured .plan-head{background:#3a4a57}
.plan.featured li{color:#cfd6dc;border-color:#3a4a57}

/* difference */
.difference{top:1730px;height:520px}
.difference h2{position:absolute;left:80px;top:110px;font-size:36px;font-weight:400}
.difference h2 .hl{color:var(--orange);font-weight:500}
.difference .text{position:absolute;left:80px;top:170px;width:520px}
.difference .text p{margin-bottom:16px}
.difference .btn{position:absolute;left:80px;top:410px}
.difference .art{position:absolute;left:650px;top:90px;width:470px;height:330px;border-radius:6px;background:linear-gradient(180deg,#e9edf0,#c8ced3)}

/* support */
.support{top:2250px;height:940px;border-top:1px solid var(--line);padding-top:90px}
.support .lede{width:1040px;margin:16px auto 0;text-align:center}
.tiles{position:absolute;left:0;top:300px;width:1200px}
.tile{position:absolute;width:300px;text-align:center}
.tile .ico{width:150px;height:150px;margin:0 auto 22px;border-radius:50%}
.tile h3{font-size:18px;font-weight:400;margin-bottom:10px}
.tile p{font-size:12px;line-height:19px;color:var(--muted)}

/* register */
.register{top:3190px;height:420px;border-top:1px solid var(--line)}
.register h2{position:absolute;left:80px;top:40px;font-size:32px;font-weight:400}
.register h2 .hl{color:var(--orange);font-weight:500}
.register .sub{position:absolute;left:80px;top:90px;font-size:13px;color:var(--muted)}
.register .field{position:absolute;left:80px;top:130px;width:460px;height:40px;border:none;border-bottom:2px solid var(--line);font-size:14px;color:var(--muted);padding:10px 2px}
.register .tlds{position:absolute;left:80px;top:190px;display:flex;gap:26px;font-size:14px}
.register .tlds span::before{content:"";display:inline-block;width:11px;height:11px;border:1px solid var(--muted);border-radius:50%;margin-right:6px;vertical-align:-1px}
.register .tlds span.on::before{background:var(--green);border-color:var(--green)}
.register .btn{position:absolute;left:80px;top:250px}
.register .art{position:absolute;left:640px;top:40px;width:500px;height:290px;border-radius:6px;background:linear-gradient(135deg,#dfe9d2,#cfd9e4)}

/* partners */
.partners{top:3610px;height:100px;background:var(--green);display:flex;align-items:center;justify-content:center;gap:30px}
.badge{width:80px;height:30px;border-radius:4px;background:rgba(255,255,255,.35)}
.badge.wide{width:320px;height:58px;background:#fff}
.badge.mid{width:240px;height:50px;background:#fff}

/* footer */
.footer{top:3710px;height:310px;background:var(--navy)}
.footer .rocket{position:absolute;left:30px;top:20px;width:190px;height:280px;border-radius:6px;background:linear-gradient(180deg,#2b3947,#f7931e)}
.fcol{position:absolute;top:40px;color:#c7ced4;font-size:13px}
.fcol h4{color:var(--green);font-size:18px;font-weight:400;margin-bottom:16px}
.fcol ul{list-style:none}
.fcol li{margin-bottom:8px}
.fcol li::before{content:"›";color:var(--green);margin-right:8px}
.pill{display:block;background:var(--green);color:#fff;border-radius:14px;padding:7px 16px;margin-bottom:12px;font-size:13px;width:220px}
.bottom{top:4020px;height:52px;background:#0c131a;color:#9aa4ad;font-size:11px;display:flex;align-items:center;justify-content:space-between;padding:0 40px}
.bottom .pay{display:flex;gap:8px;align-items:center}
.bottom .pay i{display:block;width:34px;height:20px;background:#2b3947;border-radius:3px}
</style>
</head>
<body>

<header class="section header">
  <div class="topbar">
    <span>+40 555 010 200 / +40 555 010 201</span>
    <span>Web Hosting</span>
    <span>Login Customer</span>
    <span>Support Center</span>
    <span>Contact</span>
  </div>
  <div class="logo"><div class="logo-dot"></div><div class="logo-name">brisk maple</div></div>
  <nav class="nav">
    <a class="active">Home</a><a>Web Hosting SSD</a><a>Web Hosting</a><a>Domains</a><a>VPS</a><a>Command</a><a>Support</a><a>Contact</a>
  </nav>
</header>

<section class="section hero">
  <div class="hero-art" role="img" aria-label="Illustration of hands typing on a laptop surrounded by connected web and cloud icons"></div>
  <div class="hero-copy">
    <div class="kicker">Your First Choice Of</div>
    <h1>Web Hosting</h1>
    <span class="btn">Learn More</span>
  </div>
</section>

<section class="section features">
  <div class="feature">
    <div class="ico" style="background:var(--orange)"><svg width="56" height="56" viewBox="0 0 56 56"><rect x="10" y="12" width="36" height="32" rx="4" fill="none" stroke="#fff" stroke-width="3"/><line x1="10" y1="30" x2="46" y2="30" stroke="#fff" stroke-width="3"/><circle cx="38" cy="37" r="2.5" fill="#fff"/></svg></div>
    <h3>Extreme SSD</h3>
    <p>Fast solid state storage on every plan keeps your pages quick and your data safe, with daily backups and instant recovery when needed.</p>
  </div>
  <div class="feature">
    <div class="ico" style="background:var(--teal)"><svg width="60" height="50" viewBox="0 0 60 50"><path d="M16 40h30a10 10 0 0 0 0-20 14 14 0 0 0-27-3 11 11 0 0 0-3 23z" fill="none" stroke="#fff" stroke-width="3"/></svg></div>
    <h3>DDOS Hosting</h3>
    <p>Network level filtering blocks attack traffic before it reaches you, so your sites stay online around the clock without extra setup.</p>
  </div>
  <div class="feature">
    <div class="ico" style="background:var(--blue)"><svg width="56" height="56" viewBox="0 0 56 56"><circle cx="28" cy="28" r="20" fill="none" stroke="#fff" stroke-width="3"/><ellipse cx="28" cy="28" rx="9" ry="20" fill="none" stroke="#fff" stroke-width="2"/><line x1="8" y1="28" x2="48" y2="28" stroke="#fff" stroke-width="2"/></svg></div>
    <h3>€29.90 .US Domains</h3>
    <p>Register your new name in minutes with free DNS management, privacy options and simple renewals from one clear control panel.</p>
  </div>
</section>

<section class="section pricing">
  <h2 class="title"><span class="hl">Hosting</span> Plans &amp; Pricing</h2>
  <p class="lede">Hosting packages are divided into three groups: SSD hosting for speed, standard web hosting with large space and SSL certificates for secure sites. Every plan includes support, a free setup and tools to build, manage and grow your online presence with ease.</p>
  <div class="plans">
    <div class="plan">
      <div class="plan-head"><small>Starting At</small><div class="price">€ 5.90 / month</div><div class="kind">Web Hosting SSD</div></div>
      <div class="lead">Performance up to 5x higher than the HDD-based systems</div>
      <ul><li>Packages designed for speed and efficiency</li><li>SSD drives on every server node</li><li>Performance level processors E5</li><li>Between 60-90 memory per site</li></ul>
      <span class="btn">Start Hosting Today</span>
    </div>
    <div class="plan featured">
      <div class="plan-head"><small>Starting At</small><div class="price">0.99 € / month</div><div class="kind">Web Hosting</div></div>
      <div class="lead">All web hosting packages have large space and unlimited traffic</div>
      <ul><li>Import Quality / Performance / Price Excellent</li><li>Charged for domains on domain registration</li><li>3 months free to get a discount first year</li><li>Servers in Northvale and in the EU</li></ul>
      <span class="btn">Start Hosting Today</span>
    </div>
    <div class="plan">
      <div class="plan-head"><small>Starting At</small><div class="price">€ 10.90 / year</div><div class="kind">SSL certificates</div></div>
      <div class="lead">SSL (https) provides online safety and confidence Visitors</div>
      <ul><li>Verification and issuance from 5th 2h to 24h</li><li>Full encryption SSL 256 bit (RSA 2048)</li><li>Trusted by all popular browsers and devices</li><li>Wildcard and multi domain certificates</li></ul>
      <span class="btn">Start Hosting Today</span>
    </div>
  </div>
</section>

<section class="section difference">
  <h2><span class="hl">The</span> BRISKMAPLE Difference</h2>
  <div class="text lede">
    <p>Our team has built a hosting platform around speed, stability and honest support. Every server is tuned for modern sites, monitored day and night, and backed by engineers who answer quickly and speak plainly about any issue you face.</p>
    <p>Simplicity runs through everything we offer: clear prices, no hidden fees, one dashboard for billing, domains and email. Upgrade whenever you grow, move between plans freely, and keep full control of your files and data.</p>
  </div>
  <span class="btn">Compare Plans Now</span>
  <div class="art" role="img" aria-label="Laptop showing the brand name on screen"></div>
</section>

<section class="section support">
  <h2 class="title"><span class="hl">Quick Access To</span> Technical Support</h2>
  <p class="lede">Every client receives a dedicated support team and a full library of guides. Open tickets, follow notifications, read setup articles for email, domains and backups, and reach a person whenever you need help with your account or your hosted sites.</p>
  <div class="tiles">
    <div class="tile" style="left:150px;top:0">
      <div class="ico" style="background:linear-gradient(135deg,#dbe3ea,#aebccb)" role="img" aria-label="Illustration of a support agent with headset"></div>
      <h3>Dedicated Support Team</h3><p>A team of trained technicians answers every request clearly and fast.</p>
    </div>
    <div class="tile" style="left:450px;top:0">
      <div class="ico" style="background:linear-gradient(135deg,#f4c9c3,#d9483b)" role="img" aria-label="Illustration of a phone with notification alerts"></div>
      <h3>Tracking System Notifications</h3><p>All alerts are sent instantly so you always know what is going on.</p>
    </div>
    <div class="tile" style="left:750px;top:0">
      <div class="ico" style="background:linear-gradient(135deg,#f6dfc4,#e68a2e)" role="img" aria-label="Illustration of documents and technical articles"></div>
      <h3>Relevant technical articles</h3><p>Over one hundred tutorials and articles in our support center.</p>
    </div>
    <div class="tile" style="left:300px;top:310px">
      <div class="ico" style="background:linear-gradient(135deg,#d5e8f3,#3a8dc4)" role="img" aria-label="Illustration of a person moving files between servers"></div>
      <h3>Free Assistance Transfer</h3><p>We move your sites from any other provider at no extra cost.</p>
    </div>
    <div class="tile" style="left:600px;top:310px">
      <div class="ico" style="background:linear-gradient(135deg,#e2e6ea,#5b6d7c)" role="img" aria-label="Illustration of a support center agent"></div>
      <h3>BRISKMAPLE Support Center</h3><p>Open tickets, chat and browse guides from a single place online.</p>
    </div>
  </div>
</section>

<section class="section register">
  <h2><span class="hl">Check</span> the free registration is sought</h2>
  <p class="sub">Domains are registered with your data, and the property is yours!</p>
  <div class="field">eg: example</div>
  <div class="tlds"><span class="on">.com</span><span>.eu</span><span>.net</span><span>.org</span><span>.ro</span></div>
  <span class="btn">Search Now</span>
  <div class="art" role="img" aria-label="Illustration of a website browser window with domain search"></div>
</section>

<section class="section partners">
  <div class="badge"></div><div class="badge"></div><div class="badge"></div><div class="badge"></div><div class="badge"></div><div class="badge"></div>
  <div class="badge mid"></div><div class="badge wide"></div>
</section>

<footer class="section footer">
  <div class="rocket" role="img" aria-label="Illustration of a rocket launching"></div>
  <div class="fcol" style="left:260px">
    <h4>Quick Links</h4>
    <ul><li>Home</li><li>Web Hosting SSD</li><li>Web Hosting</li><li>Domains</li><li>VPS</li><li>Command</li><li>Support</li><li>Contact</li></ul>
  </div>
  <div class="fcol" style="left:540px">
    <h4>Services</h4>
    <ul><li>Contract Delivery Services</li><li>Terms and conditions</li><li>Personal Data Protection</li><li>Card Payment</li><li>Online Dispute Resolution</li><li>Cookies information</li><li>Affiliate Program Contract</li></ul>
  </div>
  <div class="fcol" style="left:860px">
    <h4>Contact Us</h4>
    <span class="pill">Live Chat</span>
    <span class="pill">+40 555 010 200</span>
    <span class="pill">hello@briskmaple.example</span>
  </div>
</footer>

<div class="section bottom">
  <span>BRISKMAPLE LTD, 12 Orchard Lane, Suite 4, Northvale — Reg. No. 0000/2016 — All rights reserved</span>
  <span class="pay">We accept payment via <i></i><i></i><i></i><i></i></span>
</div>

</body>
</html>
```